Mind Ledger - Web Design Project

We need a website for our new company based in Sao Paulo - Brazil. Our initial product is Mind Ledger - an online assessment system based on the most recent neuroscience academic research. The system gathers tests that are applied in the selection and evaluation of employees. We would like to see designs that use the colors black and blue. The final design should communicate trust. We like clean and simple designs.

Login to www.mindledger.com.br
login: user
pass: user

We need three pages:
1- Login page: http://www.mindledger.com.br/

2- Welcome page: http://www.mindledger.com.br/sys/admin/index.php

3- Results page: http://www.mindledger.com.br/sys/admin/admin_provas_resultados.php?unique_id=5

Our logo was created using ArtQuarry.
Next projetcs: Tests interface redesign.

Industry/Entity Type

It Company

Requirements
Must have
• Link folders. i.e.:
Home :: Users :: Paul Wren :: Test1
Nice to have
• Image Buttons
Should not have
• Noise

```html
<!DOCTYPE html>
<html lang="en">
<head>
<meta charset="utf-8">
<title>Mind Ledger</title>
<link href="https://fonts.googleapis.com/css2?family=Source+Sans+3:ital,wght@0,400;0,600;0,700;1,400&display=swap" rel="stylesheet">
<style>
:root{
  --blue:#1f6fc0;
  --blue-dark:#0f4f98;
  --nav-top:#5aa5e3;
  --nav-bot:#1e6db7;
  --ink:#222;
  --text:#666;
  --rule:#dcdcdc;
  --panel:#f3f3f3;
  --hero-bg:#f2f5f9;
  --footer:#3b3b3b;
  --dark-btn:#1e1e1e;
}
*{margin:0;padding:0;box-sizing:border-box}
html,body{width:872px;height:1200px;overflow:hidden;background:#fff}
body{font-family:"Source Sans 3",sans-serif;color:var(--ink);position:relative}
.abs{position:absolute}
.top-strip{left:0;top:0;width:872px;height:4px;background:#ddd}
.logo{left:44px;top:54px;font-size:30px;font-weight:400;color:#1a1a1a;letter-spacing:-.5px}
.account-tabs{left:660px;top:4px;display:flex;gap:10px}
.account-tabs span{display:block;width:72px;height:26px;border-radius:0 0 14px 14px;font-size:11.5px;text-align:center;line-height:24px}
.tab-login{background:var(--dark-btn);color:#fff}
.tab-signup{background:#e4e4e4;color:#333}
.search{left:622px;top:59px;width:197px;height:25px;border:1px solid #ddd;font-size:9px;font-style:italic;color:#999;padding:7px 9px}
.search svg{position:absolute;right:9px;top:5px}
.nav{left:0;top:100px;width:872px;height:38px;background:linear-gradient(var(--nav-top),var(--nav-bot));display:flex;padding-left:34px}
.nav a{color:#fff;text-decoration:none;font-size:13.5px;font-weight:600;line-height:38px;padding:0 17px;border-right:1px solid rgba(0,0,0,.15);box-shadow:1px 0 0 rgba(255,255,255,.15)}
.nav a:last-child{border:0;box-shadow:none}
.hero-band{left:0;top:138px;width:872px;height:293px;background:var(--hero-bg);border-bottom:1px solid #e3e8ee}
.hero{left:32px;top:148px;width:806px;height:273px;background:#fff;border:1px solid #dfe5ec;border-radius:3px;overflow:hidden}
.hero-photo{position:absolute;right:0;top:0;width:450px;height:273px;background:linear-gradient(90deg,#fff 0%,#dfe6ee 20%,#a9c4e2 55%,#7aa3d2 75%,#cdd8e4 100%)}
.hero h1{position:absolute;left:46px;top:50px;font-size:27px;font-weight:600;color:#222}
.hero h2{position:absolute;left:47px;top:81px;font-size:16.5px;font-weight:600;color:var(--blue)}
.hero p{position:absolute;left:46px;top:107px;width:320px;font-size:9.6px;line-height:18.3px;color:var(--blue)}
.btn{position:absolute;left:46px;top:169px;width:99px;height:29px;background:var(--dark-btn);color:#fff;font-size:10px;font-weight:600;text-align:center;line-height:29px;border-radius:3px}
.dots{position:absolute;left:46px;top:217px;display:flex;gap:2px}
.dots i{width:6px;height:6px;border-radius:50%;background:#9bb8d8}
.dots i:first-child{background:var(--blue-dark)}
.crumbs{left:40px;top:442px;font-size:11.5px;color:var(--blue)}
.welcome h1{position:absolute;left:37px;top:479px;font-size:19px;font-weight:600}
.lead{left:37px;top:510px;width:540px;font-size:12.2px;line-height:17.6px;color:#222}
.body-copy{left:37px;top:553px;width:534px;font-size:9.8px;line-height:17.4px;color:var(--text);text-align:justify}
.rule{left:37px;top:663px;width:541px;height:1px;background:var(--rule)}
.section-title{font-size:15px;font-weight:600;color:var(--blue)}
.ph{background:linear-gradient(135deg,#8fa3b8,#d3dbe3 55%,#6f8398)}
.work-img{left:34px;top:733px;width:258px;height:108px}
.item-title{font-size:12px;font-weight:600;color:#222}
.small{font-size:9.8px;line-height:17.4px;color:var(--text)}
.just{text-align:justify}
.thumb{width:86px;height:82px}
.sidebar{left:624px;top:460px;width:215px;height:616px;border:1px solid #e3e3e3;border-radius:3px}
.side-head{position:absolute;left:0;width:213px;height:36px;background:var(--panel);border-bottom:1px solid #e6e6e6;font-size:15px;font-weight:600;padding:9px 17px}
.news{position:absolute;left:18px;width:190px}
.news b{display:block;font-weight:400;font-size:10px;color:var(--blue);margin-bottom:3px}
.news span{display:block;font-size:8.8px;line-height:14px;color:var(--text)}
.quote{position:absolute;left:21px;width:185px;font-size:8.8px;line-height:15.8px;font-style:italic;color:var(--text)}
.author{position:absolute;left:21px;font-size:9.5px;color:#555}
.footer{left:0;top:1104px;width:872px;height:96px;background:var(--footer)}
.foot-links{position:absolute;left:34px;top:27px;font-size:10.8px;color:#fff}
.foot-links span{margin:0 5px;color:#ccc}
.copy{position:absolute;left:35px;top:57px;font-size:8.5px;color:#ddd}
.social{position:absolute;left:750px;top:26px;display:flex;gap:2px}
.social i{width:20px;height:20px;border-radius:50%;background:#fff}
</style>
</head>
<body>
<div class="abs top-strip"></div>
<div class="abs logo">Mind Ledger</div>
<div class="abs account-tabs"><span class="tab-login">Log In</span><span class="tab-signup">Sign Up</span></div>
<div class="abs search">Search here..
<svg width="14" height="14" viewBox="0 0 14 14"><circle cx="6" cy="6" r="4.2" fill="none" stroke="#888" stroke-width="1.8"/><line x1="9" y1="9" x2="12.5" y2="12.5" stroke="#888" stroke-width="2"/></svg></div>

<nav class="abs nav">
<a>Home</a><a>About Us</a><a>Why We Are</a><a>Our Services</a><a>Results</a><a>Projects</a><a>Support</a><a>Blog</a><a>Contact Us</a>
</nav>

<div class="abs hero-band"></div>
<section class="abs hero">
  <div class="hero-photo" role="img" aria-label="Photo of a smiling businessman in a blue shirt with colleagues in an office behind him"></div>
  <h1>Online Assessment Now</h1>
  <h2>Pellentesque Ut accumsan ultricies elit</h2>
  <p>Ut ante enim, dapibus malesuada, fringilla eu, condimentum quis, tellus. Aenean porttitor eros vel dolor. Donec convallis pede venenatis nibh. Duis quam. Nam eget lacus. Aliquam erat volutpat.</p>
  <div class="btn">LEARN MORE</div>
  <div class="dots"><i></i><i></i><i></i><i></i></div>
</section>

<div class="abs crumbs">Home :: Welcome</div>
<div class="welcome"><h1>Welcome to Mind Ledger Website Mainpage..</h1></div>
<p class="abs lead">Aliquam vehicula mi at mauris. Maecenas placerat, nisl at consequat rhoncus, sem nunc gravida justo, quis eleifend arcu velit quis lacus.</p>
<p class="abs body-copy">Maecenas at justo id velit placerat molestie. Donec dictum lectus non odio. Cras a ante vitae enim iaculis aliquam. Mauris nunc quam, venenatis nec, euismod sit amet, egestas placerat, est. Pellentesque habitant morbi tristique senectus et netus et malesuada fames ac turpis egestas. Cras id elit. Integer quis urna. Ut ante enim, dapibus malesuada, fringilla eu, condimentum quis, tellus. Aenean porttitor eros vel dolor. Donec convallis pede venenatis nibh. Duis quam. Nam eget lacus. Aliquam erat volutpat.</p>
<div class="abs rule"></div>

<h3 class="abs section-title" style="left:34px;top:700px">How We Work</h3>
<div class="abs ph work-img" role="img" aria-label="Photo of business colleagues reviewing documents together"></div>
<div class="abs item-title" style="left:39px;top:851px">Aliquam erat volutpat.</div>
<p class="abs small just" style="left:39px;top:872px;width:242px">Etiam est nunc, venenatis in, tristique eu, imperdiet ac, nisl. Cum sociis natoque penatibus et magnis dis parturient montes, nascetur ridiculus mus. In iaculis facilisis massa. Etiam eu urna.</p>
<p class="abs small just" style="left:39px;top:949px;width:242px">urna. Ut ante enim, dapibus malesuada, fringilla eu, condimentum quis, tellus. Aenean porttitor eros vel dolor. Donec convallis pede venenatis nibh. Duis quam. Nam eget lacus. Aliquam erat volutpat. Quisque dignissim congue leo.3</p>

<h3 class="abs section-title" style="left:322px;top:700px">Projects &amp; Services</h3>
<div class="abs ph thumb" style="left:322px;top:733px" role="img" aria-label="Photo of a team meeting around a table"></div>
<div class="abs item-title" style="left:420px;top:731px">Aliquam erat volutpat.</div>
<p class="abs small" style="left:420px;top:753px;width:170px">Etiam est nunc, venenatis in, tristique eu, imperdiet ac, nisl. Cum sociis natoque penatibus et magnis dis</p>
<div class="abs ph thumb" style="left:322px;top:838px" role="img" aria-label="Photo of a smiling businesswoman"></div>
<div class="abs item-title" style="left:420px;top:835px">Aliquam erat volutpat.</div>
<p class="abs small" style="left:420px;top:857px;width:170px">Etiam est nunc, venenatis in, tristique eu, imperdiet ac, nisl. Cum sociis natoque penatibus et magnis dis</p>
<div class="abs ph thumb" style="left:323px;top:942px" role="img" aria-label="Photo of business people shaking hands"></div>
<div class="abs item-title" style="left:421px;top:939px">Aliquam erat volutpat.</div>
<p class="abs small" style="left:421px;top:961px;width:170px">Etiam est nunc, venenatis in, tristique eu, imperdiet ac, nisl. Cum sociis natoque penatibus et magnis dis</p>

<aside class="abs sidebar">
  <div class="side-head" style="top:0">Latest News</div>
  <div class="news" style="top:49px"><b>Donec convallis pede venenatis nibh</b><span>What would you do if you walked into your office tomorrow morning, switched on your ..</span></div>
  <div class="news" style="top:115px;left:16px"><b>Morbi magna magna</b><span>The idea of sending mission critical data over the Internet was a scary proposition for ...</span></div>
  <div class="news" style="top:178px"><b>Donec convallis pede venenatis</b><span>What would you do if you walked into your office tomorrow morning, switched on your ..</span></div>
  <div class="news" style="top:240px;left:19px"><b>Suspendisse quam leo</b><span>What would you do if you walked into your office tomorrow morning, switched on your ..</span></div>
  <div class="side-head" style="top:318px;border-top:1px solid #e6e6e6">Testimonials
    <svg width="30" height="20" viewBox="0 0 30 20" style="position:absolute;left:107px;top:9px"><ellipse cx="15" cy="8" rx="14" ry="8" fill="#d6d6d6"/><path d="M8 13 L5 19 L14 15Z" fill="#d6d6d6"/></svg></div>
  <p class="quote" style="top:369px">Ut ante enim, dapibus malesuada, fringilla eu, condimentum quis, tellus. Aenean porttitor eros vel dolor. Donec convallis pede venenatis nibh. Duis quam.</p>
  <div class="author" style="top:436px">By Author Name</div>
  <p class="quote" style="top:470px">Morbi magna magna, tincidunt a, mattis non, imperdiet vitae, tellus. Sed odio est, auctor ac, sollicitudin in, consequat vitae, orci. Fusce id felis. Vivamus sollicitudin metus eget eros.</p>
  <div class="author" style="top:563px">By Author Name</div>
</aside>

<footer class="abs footer">
  <div class="foot-links">Home<span>|</span>About Us<span>|</span>Why We Are<span>|</span>Our Services<span>|</span>Results<span>|</span>Projects<span>|</span>Support<span>|</span>Contact Us</div>
  <div class="copy">Copyright © 2013 Company Name.&nbsp; All right reserved.&nbsp; Term of Use</div>
  <div class="social"><i></i><i></i><i></i><i></i></div>
</footer>
</body>
</html>
```